New Company Business Card Design

I have a new company logo and I want a new business card design. I dont know if the logo file i attached is in the correct format or quality. We are a New York City Specialty construction Firm specializing in high risk out of the box projects. I want a simple and classy business card that people will his card is as crisp as the work his company does.

Target Market(s)

Clients in the heavy construction industry in New York City

Industry/Entity Type

Construction Company

Contact Information for Business Card

Simple Classy - DIFFERENT

Font styles to use
Other font styles liked:
• Mach the logo font in some way

Colors

Designer to choose colors to be used in the design.

Requirements
Must have
• Uniqueness
Nice to have
• Nothing particular - Just different and classy - Timeless
Should not have
• Goofy Shit or Gimmicky shit

```html
<!DOCTYPE html>
<html lang="en">
<head>
<meta charset="utf-8">
<title>Korvane Builders – Business Card</title>
<link href="https://fonts.googleapis.com/css2?family=Open+Sans:wght@400;700;800&display=swap" rel="stylesheet">
<style>
  :root {
    --backdrop: #dcd9d5;
    --card-white: #ffffff;
    --card-black: #221f20;
    --accent-blue: #1a86d6;
    --text-light: #f2f2f2;
    --boom-tone: #ececec;
  }
  html, body {
    margin: 0;
    padding: 0;
    width: 1200px;
    height: 900px;
    overflow: hidden;
    background: var(--backdrop);
  }
  .card {
    position: absolute;
    left: 150px;
    top: 172px;
    width: 900px;
    height: 555px;
    background: var(--card-white);
    box-shadow: 0 6px 24px rgba(0,0,0,0.18);
    overflow: hidden;
    font-family: "Open Sans", Arial, sans-serif;
  }
  .card-shapes {
    position: absolute;
    inset: 0;
    width: 100%;
    height: 100%;
  }
  .contact-block {
    position: absolute;
    left: 54px;
    top: 66px;
    color: var(--text-light);
  }
  .person-name {
    margin: 0;
    font-weight: 800;
    font-size: 31px;
    letter-spacing: 0.5px;
    color: var(--accent-blue);
    line-height: 1.1;
  }
  .person-title {
    margin: 2px 0 0 2px;
    font-size: 25px;
    line-height: 1.2;
  }
  .contact-list {
    list-style: none;
    margin: 30px 0 0 2px;
    padding: 0;
  }
  .contact-list li {
    display: flex;
    align-items: center;
    gap: 10px;
    font-size: 25px;
    line-height: 33px;
    white-space: nowrap;
  }
  .contact-icon {
    width: 18px;
    height: 18px;
    flex: none;
  }
  .address {
    margin: 18px 0 0 2px;
    font-size: 25px;
    line-height: 34px;
    white-space: nowrap;
  }
  .company-name {
    position: absolute;
    left: 545px;
    top: 392px;
    width: 320px;
    text-align: center;
    color: var(--accent-blue);
    font-weight: 800;
    margin: 0;
    line-height: 1;
  }
  .company-name .name-main {
    display: block;
    font-size: 64px;
    letter-spacing: 1px;
  }
  .company-name .name-sub {
    display: block;
    font-size: 21px;
    letter-spacing: 4px;
    margin-top: 8px;
  }
</style>
</head>
<body>
  <div class="card">
    <svg class="card-shapes" viewBox="0 0 652 402" preserveAspectRatio="none">
      <polygon class="dark-panel" points="0,0 520,0 322,402 0,402" fill="var(--card-black)"/>
      <polygon class="boom-area" role="img" aria-label="Crane lattice boom illustration along the diagonal edge"
               points="506,6 518,6 322,370 232,370" fill="var(--boom-tone)"/>
    </svg>

    <div class="contact-block">
      <h1 class="person-name">DANIEL CORWELL</h1>
      <p class="person-title">Managing Director</p>
      <ul class="contact-list">
        <li>
          <svg class="contact-icon" viewBox="0 0 20 20" aria-hidden="true"><path d="M2 7c0-3 3-4 8-4s8 1 8 4v2h-4V7H6v2H2z M4 10h12l1 7H3z" fill="var(--accent-blue)"/></svg>
          044-555 019 246
        </li>
        <li>
          <svg class="contact-icon" viewBox="0 0 20 20" aria-hidden="true"><path d="M5 2h10v5H5z M2 8h16v7h-3v3H5v-3H2z M7 13v3h6v-3z" fill="var(--accent-blue)"/></svg>
          044-555 019 246
        </li>
        <li>
          <svg class="contact-icon" viewBox="0 0 20 20" aria-hidden="true"><path d="M2 5h16v11H2z" fill="var(--accent-blue)"/><path d="M2 5l8 6 8-6" fill="none" stroke="var(--card-black)" stroke-width="1.5"/></svg>
          info@korvane.com
        </li>
        <li>
          <svg class="contact-icon" viewBox="0 0 20 20" aria-hidden="true"><circle cx="10" cy="10" r="8" fill="var(--accent-blue)"/><path d="M6 6c2 1 3 3 2 5l3 2-1 4M12 4c0 2 2 3 4 3" fill="none" stroke="var(--card-black)" stroke-width="1.4"/></svg>
          www.korvanebuild.com
        </li>
      </ul>
      <p class="address">480, Harbor Point Road<br>Eastvale City, 204816.</p>
    </div>

    <p class="company-name">
      <span class="name-main">KORVANE</span>
      <span class="name-sub">BUILDERS, INC.</span>
    </p>
  </div>
</body>
</html>
```